Global recruitment firm needs a design for marketing material

We need a design for our company Harrow Prime, which is a global recruitment firm specializing in senior finance and executive positions. This will be a template/ background for all our marketing material. We are looking to communicate a consistent message to current and existing clients. Uploaded below are our files describing our mission, values and strategy and story. Please also look at our website www.harrowprime.com.au. Examples of where this design will be used will be in client proposals, marketing info telling our story, social media content, infographics, and general client communication.

Target Market(s)

Client companies in the finance industry, Executive level finance candidates(CEO, CFO)

Requirements
Must have
• company logo, mission, value, strategy, website, our story
• Will be using the graphic for website, all communication with clients > looking for something to use for different purposes

```html
<!DOCTYPE html>
<html lang="en">
<head>
<meta charset="utf-8">
<title>Harrow Prime – Connecting Talent with Opportunity Globally</title>
<link rel="stylesheet" href="https://fonts.googleapis.com/css2?family=Montserrat:wght@400;600;700&family=Lato:wght@300;400&display=swap">
<style>
  :root {
    --sky: #4aa9dc;
    --sky-light: #a9d5ee;
    --page: #eef0f2;
    --band: #e2e8ef;
    --ink: #3d4046;
    --muted: #676b72;
    --yellow: #f2b539;
    --yellow-deep: #f6c24a;
    --teal: #33c19a;
    --blue: #4a7fe0;
    --footer: #3b3b3d;
    --footer-text: #d5d7da;
    --link: #5aa7ea;
  }
  * { margin: 0; padding: 0; box-sizing: border-box; }
  html, body { width: 1200px; height: 3600px; overflow: hidden; }
  body {
    position: relative;
    background: var(--page);
    font-family: "Lato", Arial, sans-serif;
    color: var(--ink);
  }
  .abs { position: absolute; }

  /* Header */
  .header { left: 0; top: 0; width: 1200px; height: 252px; }
  .headline {
    left: 84px; top: 54px; color: #fff;
    font-family: "Montserrat", Arial, sans-serif;
    font-size: 52px; line-height: 70px; font-weight: 400;
  }
  .headline strong { font-weight: 700; }
  .brand {
    left: 960px; top: 96px; width: 210px; text-align: center;
    font-family: "Montserrat", Arial, sans-serif; font-weight: 700;
    font-size: 30px; line-height: 36px; color: #1f5d9e; letter-spacing: 2px;
  }

  /* Hero photo */
  .hero { left: 0; top: 252px; width: 1200px; height: 580px; }
  .strategy-label {
    left: 55px; top: 730px;
    font-family: "Montserrat", Arial, sans-serif; font-weight: 600;
    font-size: 32px; color: #23405e;
  }

  /* Strategy */
  .step { top: 866px; width: 340px; text-align: center; }
  .step svg { display: block; margin: 0 auto; }
  .step-title {
    position: absolute; left: 0; right: 0; top: 190px;
    color: #fff; font-family: "Montserrat", Arial, sans-serif;
    font-weight: 600; font-size: 37px;
  }
  .step-text {
    margin-top: 36px; font-size: 26px; line-height: 35px;
    color: var(--muted); font-weight: 400;
  }

  /* Content sections */
  .band { left: 0; width: 1200px; }
  .section-title {
    font-family: "Montserrat", Arial, sans-serif; font-weight: 600;
    font-size: 37px; color: var(--ink);
  }
  .section-title .dash { font-weight: 400; color: var(--muted); }
  .section-text { font-size: 27px; line-height: 43px; color: var(--muted); }

  .story-title { left: 504px; top: 1498px; }
  .story-text { left: 504px; top: 1570px; width: 590px; }
  .mission-title { left: 137px; top: 1993px; }
  .mission-text { left: 137px; top: 2064px; width: 580px; }
  .value-title { left: 0; top: 2503px; width: 1200px; text-align: center; }
  .value-text { left: 150px; top: 2576px; width: 900px; text-align: center; }

  /* Footer */
  .footer { left: 0; top: 3190px; width: 1200px; height: 410px; }
  .contact {
    left: 0; top: 3333px; width: 1200px; text-align: center;
    font-size: 29px; color: var(--footer-text);
  }
  .contact b { color: var(--link); font-weight: 400; }
  .contact .gap { display: inline-block; width: 40px; }
  .copyright {
    left: 0; top: 3491px; width: 1200px; text-align: center;
    font-size: 27px; color: var(--footer-text);
  }
</style>
</head>
<body>

  <!-- Header -->
  <svg class="abs header" viewBox="0 0 1200 252" aria-hidden="true">
    <rect width="1200" height="252" fill="#e9ecef"/>
    <polygon points="0,0 770,0 960,252 0,252" fill="var(--sky)"/>
    <polygon points="770,0 1010,0 1100,120 960,252" fill="#d7dde3"/>
  </svg>
  <h1 class="abs headline">Connecting Talent<br>with <strong>Opportunity Globally</strong></h1>
  <div class="abs brand">HARROW<br>PRIME</div>

  <!-- Hero -->
  <svg class="abs hero" viewBox="0 0 1200 580" role="img" aria-label="Photo of a team of four professionals meeting in a bright office">
    <defs>
      <linearGradient id="heroTone" x1="0" y1="0" x2="1" y2="1">
        <stop offset="0" stop-color="#d9dcdc"/>
        <stop offset="0.5" stop-color="#b9b3aa"/>
        <stop offset="1" stop-color="#8f8a86"/>
      </linearGradient>
    </defs>
    <rect width="1200" height="580" fill="url(#heroTone)"/>
    <polygon points="0,360 0,580 480,580" fill="var(--sky-light)"/>
    <polygon points="0,580 1200,460 1200,580" fill="var(--page)"/>
  </svg>
  <div class="abs strategy-label">Our Strategy</div>

  <!-- Strategy steps -->
  <div class="abs step" style="left:99px">
    <svg width="340" height="340" viewBox="0 0 340 340" aria-hidden="true">
      <circle cx="170" cy="200" r="139" fill="var(--yellow)"/>
      <circle cx="170" cy="63" r="62" fill="var(--yellow-deep)" stroke="#f4f4f4" stroke-width="4"/>
      <g fill="none" stroke="#fff" stroke-width="7" stroke-linecap="round" stroke-linejoin="round">
        <path d="M138 78 L160 56 L178 66 L200 46"/>
        <path d="M148 88 L170 66 M160 92 L178 74 M172 94 L186 80"/>
      </g>
      <path d="M160 275 L170 285 L180 275" fill="none" stroke="#fff" stroke-width="4"/>
    </svg>
    <div class="step-title">Engage</div>
    <p class="step-text">We engage with<br>our Clients to under-<br>stand their story.</p>
  </div>

  <div class="abs step" style="left:430px">
    <svg width="340" height="340" viewBox="0 0 340 340" aria-hidden="true">
      <circle cx="170" cy="200" r="139" fill="var(--teal)"/>
      <circle cx="170" cy="63" r="62" fill="#3ccaa3" stroke="#f4f4f4" stroke-width="4"/>
      <circle cx="170" cy="63" r="30" fill="none" stroke="#fff" stroke-width="7"/>
      <circle cx="170" cy="63" r="14" fill="none" stroke="#fff" stroke-width="6"/>
      <circle cx="170" cy="63" r="4" fill="#fff"/>
      <path d="M173 60 L200 33 M192 30 L202 30 L202 40" fill="none" stroke="#fff" stroke-width="5" stroke-linecap="round"/>
      <path d="M160 275 L170 285 L180 275" fill="none" stroke="#fff" stroke-width="4"/>
    </svg>
    <div class="step-title">Challenge</div>
    <p class="step-text">Working as a<br>team, we challenge<br>finance and risk.</p>
  </div>

  <div class="abs step" style="left:759px">
    <svg width="340" height="340" viewBox="0 0 340 340" aria-hidden="true">
      <circle cx="170" cy="200" r="139" fill="var(--blue)"/>
      <circle cx="170" cy="63" r="62" fill="#5b8ee8" stroke="#f4f4f4" stroke-width="4"/>
      <path d="M168 56 L168 98 L178 88 L186 104 L193 100 L185 85 L199 84 Z" fill="#fff"/>
      <g stroke="#fff" stroke-width="5" stroke-linecap="round">
        <path d="M150 38 L156 45 M168 28 L168 38 M186 38 L180 45 M140 58 L150 58"/>
      </g>
      <path d="M160 275 L170 285 L180 275" fill="none" stroke="#fff" stroke-width="4"/>
    </svg>
    <div class="step-title">Select</div>
    <p class="step-text">We select a<br>shortlist from our<br>global network.</p>
  </div>

  <!-- Our Story -->
  <svg class="abs band" style="top:1390px" width="1200" height="550" viewBox="0 0 1200 550" aria-hidden="true">
    <polygon points="0,30 1200,0 1200,540 0,550" fill="var(--band)"/>
    <line x1="0" y1="30" x2="1200" y2="0" stroke="#d3d8de" stroke-width="3"/>
  </svg>
  <svg class="abs" style="left:128px;top:1500px" width="290" height="330" viewBox="0 0 290 330" role="img" aria-label="Photo of two professionals shaking hands across a desk">
    <defs>
      <linearGradient id="storyTone" x1="0" y1="0" x2="1" y2="1">
        <stop offset="0" stop-color="#e7d3bd"/>
        <stop offset="1" stop-color="#8d7a6a"/>
      </linearGradient>
    </defs>
    <path d="M60 30 Q140 -10 230 40 Q290 80 278 180 Q262 290 150 318 Q40 330 14 230 Q-10 100 60 30 Z" fill="url(#storyTone)" stroke="var(--yellow)" stroke-width="5"/>
  </svg>
  <h2 class="abs section-title story-title">Our Story <span class="dash">----</span></h2>
  <p class="abs section-text story-text">30 years of experience enables us to partner with our clients to challenge the recruitment strategy on people, positions and the process, to build high performing finance teams ...</p>

  <!-- Our Mission -->
  <svg class="abs band" style="top:1930px" width="1200" height="460" viewBox="0 0 1200 460" aria-hidden="true">
    <rect width="1200" height="460" fill="#eceef1"/>
  </svg>
  <h2 class="abs section-title mission-title">Our Mission <span class="dash">----</span></h2>
  <p class="abs section-text mission-text">Harrow Prime is a global search firm originating in Sydney in 2010 and today partnering with finance professionals in Australia, Hong Kong, Singapore, India, London, United States and Canada ...</p>
  <svg class="abs" style="left:748px;top:1960px" width="324" height="362" viewBox="0 0 324 362" role="img" aria-label="Photo of hands joining coloured puzzle pieces">
    <defs>
      <radialGradient id="missionTone" cx="0.5" cy="0.5" r="0.6">
        <stop offset="0" stop-color="#6fa7a6"/>
        <stop offset="1" stop-color="#1d5e74"/>
      </radialGradient>
    </defs>
    <path d="M90 20 Q200 -10 290 60 Q330 110 310 200 Q280 320 170 350 Q60 362 20 260 Q-10 150 30 80 Q50 35 90 20 Z" fill="url(#missionTone)" stroke="var(--teal)" stroke-width="5"/>
  </svg>

  <!-- Our Value -->
  <svg class="abs band" style="top:2386px" width="1200" height="820" viewBox="0 0 1200 820" aria-hidden="true">
    <polygon points="0,0 1200,12 1200,820 0,820" fill="var(--band)"/>
    <line x1="0" y1="0" x2="1200" y2="12" stroke="#d3d8de" stroke-width="3"/>
  </svg>
  <h2 class="abs section-title value-title"><span class="dash">--</span> Our Value <span class="dash">--</span></h2>
  <p class="abs section-text value-text">There are many variations of passages of lorem site that Lorem Ipsum available, but the majority have suffered alteration in form, by injected humour then proud to be ...</p>
  <svg class="abs" style="left:196px;top:2745px" width="770" height="370" viewBox="0 0 770 370" role="img" aria-label="Mockup of the design shown on desktop, laptop, tablet and phone screens">
    <defs>
      <linearGradient id="deviceTone" x1="0" y1="0" x2="0" y2="1">
        <stop offset="0" stop-color="#4aa9dc"/>
        <stop offset="0.3" stop-color="#c9cdd0"/>
        <stop offset="1" stop-color="#e7e9ec"/>
      </linearGradient>
    </defs>
    <rect x="0" y="0" width="770" height="370" rx="6" fill="url(#deviceTone)"/>
  </svg>

  <!-- Footer -->
  <svg class="abs footer" viewBox="0 0 1200 410" aria-hidden="true">
    <polygon points="0,48 1200,0 1200,410 0,410" fill="var(--footer)"/>
    <polygon points="700,28 1200,8 1200,0 " fill="#4f6f8c"/>
    <line x1="150" y1="242" x2="490" y2="242" stroke="#9a9c9f" stroke-width="2"/>
    <line x1="710" y1="242" x2="1050" y2="242" stroke="#9a9c9f" stroke-width="2"/>
    <circle cx="540" cy="242" r="23" fill="#8e9094"/>
    <circle cx="600" cy="242" r="23" fill="var(--link)"/>
    <circle cx="660" cy="242" r="23" fill="#8e9094"/>
  </svg>
  <p class="abs contact"><b>Phone:</b> +61 400-555-218<span class="gap"></span><b>Email:</b> hello@harrowprime.com.au</p>
  <p class="abs copyright">© 2018 Harrow Prime.&nbsp;&nbsp;&nbsp; | &nbsp;&nbsp;&nbsp;www.harrowprime.com.au</p>

</body>
</html>
```